Corrigan & Hale, LLC
Business Cards & Stationery
Corrigan & Hale, LLC -
Creative Brief
Professional
Deborah L. Corrigan
Attorney At Law
418 W. Brookfield Avenue Suite 3B Pearl River, New York 10965-2274
dcorrigan@corriganandhale-example.com
www.corriganandhale-example.com
We will need to be able to use template for other people in the firm.
Specializing in Civil Litigation, Wills, Trusts & Estates, Guardianships, and related matters

```html
<!DOCTYPE html>
<html lang="en">
<head>
<meta charset="utf-8">
<title>Corrigan &amp; Hale, LLC — Business Cards</title>
<link rel="stylesheet" href="https://fonts.googleapis.com/css2?family=EB+Garamond:wght@400;500;600&display=swap">
<style>
  :root {
    --backdrop: #5d5e60;
    --green: #1d5a2b;
    --green-deep: #14441f;
    --ink: #111;
    --paper: #ffffff;
    --paper-shade: #eef0ee;
    --faint: rgba(0,0,0,0.06);
    --faint-light: rgba(255,255,255,0.07);
  }
  * { margin: 0; padding: 0; box-sizing: border-box; }
  html, body { width: 1200px; height: 957px; overflow: hidden; }
  body {
    background: var(--backdrop);
    font-family: "EB Garamond", Georgia, serif;
    position: relative;
  }
  .card {
    position: absolute;
    width: 540px;
    height: 310px;
    border-radius: 12px;
    overflow: hidden;
    box-shadow: 0 10px 24px rgba(0,0,0,0.35);
  }
  .card-front { left: 330px; top: 90px; background: var(--paper); }
  .card-back-green { left: 78px; top: 595px; background: linear-gradient(160deg, var(--green), var(--green-deep)); }
  .card-back-white { left: 640px; top: 450px; background: linear-gradient(160deg, var(--paper), var(--paper-shade)); }

  .wave { position: absolute; inset: 0; }

  .brand { position: absolute; display: flex; align-items: center; gap: 12px; }
  .brand-mark { width: 34px; height: 34px; background: var(--green); }
  .brand-name {
    font-weight: 500;
    font-size: 24px;
    letter-spacing: 0.5px;
    color: var(--green);
    text-transform: uppercase;
    line-height: 1;
  }
  .brand-tag {
    display: block;
    margin-top: 5px;
    padding-top: 4px;
    border-top: 1px solid currentColor;
    font-size: 9px;
    letter-spacing: 3px;
    text-align: right;
    text-transform: uppercase;
  }
  .card-front .brand { left: 30px; top: 34px; }
  .card-front .brand-tag { color: var(--ink); }

  .details { position: absolute; left: 0; right: 0; top: 188px; color: var(--paper); }
  .person {
    position: absolute; right: 272px; top: 0;
    text-align: right; font-size: 10.5px; line-height: 1.35;
  }
  .person-name { font-size: 18px; font-weight: 500; line-height: 1.2; }
  .person-title { font-size: 12px; }
  .divider {
    position: absolute; left: 278px; top: 4px; width: 1px; height: 92px;
    background: rgba(255,255,255,0.7);
  }
  .contact {
    position: absolute; left: 288px; top: 8px;
    list-style: none; font-size: 10px; line-height: 1.55;
  }

  .ghost-square { position: absolute; left: 60px; top: 30px; width: 170px; height: 170px; }
  .card-back-green .ghost-square { background: var(--faint-light); }
  .card-back-white .ghost-square { background: var(--faint); }

  .card-back-green .brand, .card-back-white .brand { right: 30px; bottom: 44px; }
  .card-back-green .brand-name, .card-back-green .brand-tag { color: var(--paper); }
  .card-back-white .brand-tag { color: var(--ink); }
  .brand-back .brand-name { font-size: 20px; }
</style>
</head>
<body>

  <section class="card card-front" aria-label="Business card front">
    <svg class="wave" viewBox="0 0 540 310" preserveAspectRatio="none" aria-hidden="true">
      <path d="M0,140 C150,95 300,175 540,105 L540,112 C300,182 150,102 0,147Z" fill="#b9bcb9"/>
      <path d="M0,150 C150,105 300,185 540,115 L540,132 C300,202 150,122 0,167Z" fill="#111"/>
      <path d="M0,167 C150,122 300,202 540,132 L540,310 L0,310Z" fill="#1d5a2b"/>
    </svg>
    <div class="brand">
      <span class="brand-mark"></span>
      <div>
        <span class="brand-name">Corrigan &amp; Hale, LLC</span>
        <span class="brand-tag">Attorneys at Law</span>
      </div>
    </div>
    <div class="details">
      <div class="person">
        <div class="person-name">Deborah L. Corrigan</div>
        <div class="person-title">Attorney At Law</div>
        <div>418 W. Brookfield Avenue</div>
        <div>Suite 3B</div>
        <div>Maple Hollow, Vermont 05999-2274</div>
      </div>
      <span class="divider"></span>
      <ul class="contact">
        <li>P: 555.014.2267</li>
        <li>F: 555.014.3381</li>
        <li>E: dcorrigan@corriganandhale-example.com</li>
        <li>www.corriganandhale-example.com</li>
      </ul>
    </div>
  </section>

  <section class="card card-back-green" aria-label="Business card back, green">
    <span class="ghost-square"></span>
    <div class="brand brand-back">
      <div>
        <span class="brand-name">Corrigan &amp; Hale, LLC</span>
        <span class="brand-tag">Attorneys at Law</span>
      </div>
    </div>
  </section>

  <section class="card card-back-white" aria-label="Business card back, white">
    <span class="ghost-square"></span>
    <div class="brand brand-back">
      <div>
        <span class="brand-name">Corrigan &amp; Hale, LLC</span>
        <span class="brand-tag">Attorneys at Law</span>
      </div>
    </div>
  </section>

</body>
</html>
```